Newspaper Ad for Cool Hawaiian PPE Company

We need an incredible ad for our local newspaper to tell everyone about BreezeGuard.net. We want a beautiful ad that is sophisticated with a local flair. Less is more. Clean. Stands out. We are safely shipping masks and PPE to our local community. Everyone has access to the supplies they need to keep them and their loved ones safe during the pandemic. Make it really pop.

Target Market(s)

Community members

Requirements
Must have
• Half Page:

Specs 9.7” x 10” column inches for the half page. Minimum 300 dpi, jpeg is fine.

```html
<!DOCTYPE html>
<html lang="en">
<head>
<meta charset="utf-8">
<title>BreezeGuard.net – Personal Protective Equipment</title>
<link href="https://fonts.googleapis.com/css2?family=Barlow+Condensed:wght@500;700&family=Barlow:wght@400;700&family=Caveat:wght@500&display=swap" rel="stylesheet">
<style>
  :root {
    --page: #f0f0eb;
    --cream: #fdf5dc;
    --blue: #1e95d8;
    --sky: #0f96dc;
    --red: #e8323c;
    --sun: #fdd835;
    --ink: #3a3a3a;
    --rule: #bdbab2;
    --grey: #777777;
    --pink: #ef5a7a;
    --white: #ffffff;
  }
  * { margin: 0; padding: 0; box-sizing: border-box; }
  html, body { width: 1200px; height: 900px; overflow: hidden; background: var(--page); }
  .ad {
    position: absolute; left: 250px; top: 90px; width: 698px; height: 718px;
    overflow: hidden; background: var(--cream);
    box-shadow: 0 2px 10px rgba(0,0,0,.12);
  }
  .ad-art { position: absolute; inset: 0; z-index: 1; }
  .headline, .tagline, .brand-name, .trust-band, .delivery-flag, .shipping-badge { z-index: 2; }
  .headline {
    position: absolute; left: 0; top: 36px; width: 392px; text-align: center;
    font-family: "Barlow Condensed", sans-serif; font-weight: 700;
    font-size: 62px; line-height: 55px; color: var(--blue); letter-spacing: 0;
  }
  .tagline {
    position: absolute; left: 0; top: 212px; width: 392px; text-align: center;
    font-family: "Caveat", cursive; font-weight: 500; font-size: 35px; color: var(--ink);
  }
  .product-list {
    position: absolute; left: 0; top: 283px; width: 400px; list-style: none; z-index: 0;
    font-family: "Barlow", sans-serif; font-size: 16px; color: var(--ink);
  }
  .product-list li {
    display: flex; align-items: center; gap: 8px; height: 30.6px; white-space: nowrap;
  }
  .product-list li::before, .product-list li::after {
    content: ""; flex: 1; height: 1.5px; background: var(--rule);
  }
  .brand-name {
    position: absolute; left: 0; top: 618px; width: 400px; text-align: center;
    font-family: "Barlow", sans-serif; font-weight: 700; font-size: 34px;
    color: var(--grey); letter-spacing: -0.5px;
  }
  .trust-band {
    position: absolute; left: 0; bottom: 0; width: 402px; height: 34px;
    background: var(--pink); color: var(--white); white-space: nowrap;
    font-family: "Barlow Condensed", sans-serif; font-weight: 500; font-size: 20px;
    line-height: 34px; padding-left: 22px;
  }
  .delivery-flag {
    position: absolute; right: 14px; top: 10px; text-align: center; color: var(--white);
    font-family: "Barlow Condensed", sans-serif; line-height: 1;
  }
  .delivery-flag strong { display: block; font-size: 34px; font-weight: 700; }
  .delivery-flag span { display: block; font-size: 19px; font-weight: 500; }
  .shipping-badge {
    position: absolute; left: 597px; top: 88px; width: 100px; text-align: center;
    font-family: "Barlow Condensed", sans-serif; line-height: 1.05; color: var(--ink);
  }
  .shipping-badge strong { display: block; font-size: 28px; font-weight: 700; color: var(--red); }
  .shipping-badge span { display: block; font-size: 20px; font-weight: 500; }
</style>
</head>
<body>
<main class="ad">
  <ul class="product-list">
    <li>Masks (for adults &amp; children)</li>
    <li>Face Shields (for adults &amp; children)</li>
    <li>Fashion Masks</li>
    <li>Gloves</li>
    <li>Thermoters</li>
    <li>No Touch Tools</li>
    <li>Sanitizers</li>
    <li>Disinfectants</li>
  </ul>

  <svg class="ad-art" viewBox="0 0 698 718" width="698" height="718">
    <defs>
      <linearGradient id="photo-tones" x1="0" y1="0" x2="0.3" y2="1">
        <stop offset="0" stop-color="#5a4438"/>
        <stop offset="0.35" stop-color="#b08a76"/>
        <stop offset="0.65" stop-color="#8e8a88"/>
        <stop offset="1" stop-color="#c2365a"/>
      </linearGradient>
      <path id="photo-shape" d="M362 150 Q372 62 482 58 Q600 60 650 170 Q698 240 698 300 L698 718 L352 718 Q342 500 350 330 Q356 220 362 150 Z"/>
    </defs>
    <rect class="sky-panel" x="402" y="0" width="296" height="300" fill="var(--sky)"/>
    <g class="photo-halo" fill="none">
      <use href="#photo-shape" stroke="#fbf3b0" stroke-width="44"/>
      <use href="#photo-shape" stroke="#d3ead9" stroke-width="30"/>
      <use href="#photo-shape" stroke="#a9d8bf" stroke-width="14"/>
    </g>
    <use class="photo" role="img" aria-label="Photo of a smiling girl wearing a patterned face mask and holding a dragon fruit" href="#photo-shape" fill="url(#photo-tones)"/>
    <polygon class="corner-flag" points="555,0 698,0 698,150" fill="var(--red)"/>
    <polygon class="badge-star" fill="var(--sun)" points="699,128 690.5,139.7 692,154 678.8,159.8 673,173 658.7,171.5 647,180 635.3,171.5 621,173 615.2,159.8 602,154 603.5,139.7 595,128 603.5,116.3 602,102 615.2,96.2 621,83 635.3,84.5 647,76 658.7,84.5 673,83 678.8,96.2 692,102 690.5,116.3"/>
  </svg>

  <h1 class="headline">PERSONAL<br>PROTECTIVE<br>EQUIPMENT</h1>
  <p class="tagline">for family &amp; business</p>

  <p class="brand-name">BreezeGuard.net</p>
  <p class="trust-band">Hawaii's Trusted Healthcare Company for 25 Years</p>

  <div class="delivery-flag"><strong>Fast</strong><span>Delivery</span></div>
  <div class="shipping-badge"><strong>Free</strong><span>Shipping in Hawaii</span></div>
</main>
</body>
</html>
```